Architecture firm needing a business card

We need a business card design for a new company based in the US called "Dorrance Architecture". Seeking minimalist designs that have a creativity/design feel but must be clean and professional. Please refer to the logo attached.

Target Market(s)

Real Estate Investors, Home Builders and Construction Firms.

Industry/Entity Type

Architecture

Contact Information for Business Card

Standard US size business cards. Would like to have some sort of graphic on the back side of the card - nothing that is too loud but something that may catch your attention. More or less grayscale colors that are in line with the logo colors (navy and greys essentially). Additional colors maybe accepted if blended properly (earthtones), but might be difficult to accomplish and maintain the clean/minimalist look.

Requirements
Must have
• Clean Lines
Nice to have
• some sort of graphics, would like to have something creative on the back side of the card
Should not have
• nothing too busy, cluttered or overwhelming.

```html
<!DOCTYPE html>
<html lang="en">
<head>
<meta charset="UTF-8">
<title>Dorrance Architecture – Business Card</title>
<link href="https://fonts.googleapis.com/css2?family=Open+Sans:wght@400;700&display=swap" rel="stylesheet">
<style>
  :root {
    --navy: #1f3a5c;
    --ink: #000000;
    --charcoal: #3d3d3d;
    --white: #ffffff;
    --logo-grey: #7d8a99;
    --page: #ffffff;
  }
  html, body {
    margin: 0;
    padding: 0;
    width: 1200px;
    height: 244px;
    overflow: hidden;
    background: var(--page);
  }
  .canvas {
    position: relative;
    width: 1200px;
    height: 244px;
    font-family: "Open Sans", Arial, sans-serif;
  }
  .card {
    position: absolute;
    top: 0;
    width: 422px;
    height: 244px;
    overflow: hidden;
  }
  .card-accent {
    position: absolute;
    left: 0;
    top: 0;
    width: 21px;
    height: 100%;
    background: var(--navy);
  }
  /* Front */
  .card-front {
    left: 0;
    background: linear-gradient(90deg, var(--charcoal) 0%, #1c1c1c 55%, var(--ink) 100%);
  }
  .holder {
    position: absolute;
    left: 52px;
    top: 106px;
    color: var(--white);
    font-weight: 700;
    font-size: 13px;
    line-height: 23px;
  }
  .holder p { margin: 0; }
  /* Back */
  .card-back {
    left: 488px;
    background: var(--ink);
  }
  .backdrop {
    position: absolute;
    left: 80px;
    top: 0;
    width: 342px;
    height: 244px;
    background:
      radial-gradient(ellipse 90px 100px at 270px 150px, #e8e8e8 0%, #a9a9a9 35%, #3a3a3a 70%, transparent 100%),
      radial-gradient(ellipse 260px 220px at 300px 90px, #2b2b2b 0%, #141414 55%, transparent 100%);
  }
  .brand {
    position: absolute;
    left: 38px;
    top: 124px;
    display: flex;
    align-items: center;
    gap: 8px;
    color: var(--logo-grey);
    font-weight: 400;
  }
  .brand-square {
    width: 30px;
    height: 30px;
    background: var(--navy);
  }
  .brand-name {
    font-size: 17px;
    line-height: 17px;
    letter-spacing: 1px;
    text-transform: uppercase;
  }
  .brand-name span {
    display: block;
    font-size: 8px;
    line-height: 12px;
    letter-spacing: 2px;
  }
</style>
</head>
<body>
<main class="canvas">
  <section class="card card-front">
    <div class="card-accent"></div>
    <div class="holder">
      <p class="holder-name">Nora Whitfield</p>
      <p class="holder-title">Senior Architect</p>
    </div>
  </section>

  <section class="card card-back">
    <div class="backdrop" role="img" aria-label="Black and white photograph of receding white arches in a dark corridor"></div>
    <div class="card-accent"></div>
    <div class="brand">
      <div class="brand-square"></div>
      <div class="brand-name">Dorrance<span>Architecture</span></div>
    </div>
  </section>
</main>
</body>
</html>
```